Boutique custom software development company needs new business card

Our nearly 20 year old custom software development company would like to better include the fact that we are now providing Bitcoin services. These new services are B2B include education (how to acquire and securely hold Bitcoin) and integrating Bitcoin payments into existing ecommerce sites or other existing systems. Please keep the card clean and simple. Attached is our current design and some other files. vexalon.example

Target Market(s)

businesses owners interested in long term relationship

Industry/Entity Type

Custom software development and Bitcoin

Contact Information for Business Card

Marcus Ellwood, marcus@vexalon.example, vexalon.example, (888) 555-VEXAL

Font styles to use
Other font styles liked:
• monospace

Requirements
Must have
• double-sided
Nice to have
• clean and simple
Should not have
• physical address

```html
<!DOCTYPE html>
<html lang="en">
<head>
<meta charset="utf-8">
<title>Vexalon Business Card</title>
<link href="https://fonts.googleapis.com/css2?family=Lato:wght@400;700&family=Anton&family=Work+Sans:wght@500&display=swap" rel="stylesheet">
<style>
  :root {
    --bg: #e9e9ea;
    --card-white: #f6f6f4;
    --brand-blue: #5583c2;
    --brand-orange: #ef8433;
    --ink-white: #ffffff;
  }
  * { box-sizing: border-box; margin: 0; padding: 0; }
  html, body { width: 1200px; height: 905px; overflow: hidden; }
  body {
    background: var(--bg);
    position: relative;
    font-family: "Lato", sans-serif;
  }
  .card {
    position: absolute;
    left: 320px;
    width: 560px;
    height: 320px;
    border-radius: 22px;
    overflow: hidden;
    box-shadow: 0 10px 24px rgba(0,0,0,0.12);
  }
  .card--front { top: 62px; background: var(--card-white); }
  .card--back { top: 462px; background: var(--brand-blue); }
  .corner-tab {
    position: absolute;
    left: 0;
    top: 60px;
    width: 80px;
    height: 100px;
    background: var(--brand-orange);
    clip-path: polygon(0 0, 100% 0, 80% 100%, 0 100%);
  }
  .brand-block {
    position: absolute;
    left: 140px;
    top: 80px;
  }
  .brand-name {
    font-family: "Lato", sans-serif;
    font-weight: 700;
    font-size: 76px;
    letter-spacing: 1px;
    line-height: 1;
    color: var(--brand-blue);
  }
  .brand-tagline {
    margin-top: 12px;
    font-family: "Lato", sans-serif;
    font-weight: 400;
    font-size: 22px;
    line-height: 1.2;
    color: var(--brand-blue);
  }
  .brand-service {
    margin-top: 8px;
    font-family: "Lato", sans-serif;
    font-weight: 700;
    font-size: 15px;
    letter-spacing: 0.5px;
    color: var(--brand-orange);
  }
  .back-brand {
    position: absolute;
    left: 108px;
    top: 84px;
    font-family: "Lato", sans-serif;
    font-weight: 700;
    font-size: 42px;
    line-height: 1;
    color: var(--ink-white);
    letter-spacing: 1px;
  }
  .back-service {
    position: absolute;
    left: 108px;
    top: 136px;
    width: 200px;
    font-family: "Lato", sans-serif;
    font-weight: 400;
    font-size: 14px;
    line-height: 1.35;
    color: var(--ink-white);
  }
  .divider {
    position: absolute;
    left: 330px;
    top: 150px;
    width: 2px;
    height: 140px;
    background: var(--ink-white);
  }
  .contact {
    position: absolute;
    left: 348px;
    top: 170px;
    color: var(--ink-white);
  }
  .contact-name {
    font-family: "Anton", sans-serif;
    font-size: 26px;
    line-height: 1.2;
    letter-spacing: 0.5px;
    margin-bottom: 8px;
  }
  .contact-line {
    display: flex;
    align-items: center;
    gap: 7px;
    font-family: "Work Sans", sans-serif;
    font-weight: 500;
    font-size: 14px;
    line-height: 24px;
    white-space: nowrap;
  }
  .contact-line svg { width: 14px; height: 14px; flex: none; }
</style>
</head>
<body>
  <section class="card card--front">
    <div class="corner-tab"></div>
    <div class="brand-block">
      <div class="brand-name">VEXALON</div>
      <div class="brand-tagline">developer of custom applications</div>
      <div class="brand-service">Bitcoin education &amp; payment integration</div>
    </div>
  </section>

  <section class="card card--back">
    <div class="corner-tab"></div>
    <div class="back-brand">VEXALON</div>
    <div class="back-service">Custom software &amp; B2B Bitcoin services</div>
    <div class="divider"></div>
    <div class="contact">
      <div class="contact-name">Marcus Ellwood</div>
      <div class="contact-line">
        <svg viewBox="0 0 16 16"><circle cx="8" cy="8" r="8" fill="#fff"/><rect x="4" y="5" width="8" height="6" fill="none" stroke="#5583c2" stroke-width="1.2"/><path d="M4 5l4 3.5L12 5" fill="none" stroke="#5583c2" stroke-width="1.2"/></svg>
        marcus@vexalon.example
      </div>
      <div class="contact-line">
        <svg viewBox="0 0 16 16"><circle cx="8" cy="8" r="8" fill="#fff"/><circle cx="8" cy="8" r="4.5" fill="none" stroke="#5583c2" stroke-width="1.2"/><path d="M3.5 8h9M8 3.5v9" stroke="#5583c2" stroke-width="1.1"/></svg>
        vexalon.example
      </div>
      <div class="contact-line">
        <svg viewBox="0 0 16 16"><circle cx="8" cy="8" r="8" fill="#fff"/><path d="M5.5 4.2l1.6-.2.8 2-1 .9a5 5 0 0 0 2.2 2.2l.9-1 2 .8-.2 1.6c-.3.5-1 .8-1.6.7A6.5 6.5 0 0 1 4.8 5.8c-.1-.6.2-1.3.7-1.6z" fill="#5583c2"/></svg>
        (888) 555-VEXAL
      </div>
    </div>
  </section>
</body>
</html>
```